We need a business card design for a Dubai based company .

We need a business card for a Dubai based company called "Zernova Smoking Requisites Trading LLC". We mainly import Flavoured Tobacco products and Charcoal which is used for smoking in a Hookah/Shisha and distribute to the wholesalers and retailers. Logo file is attached herewith.

```html
<!DOCTYPE html>
<html lang="en">
<head>
<meta charset="utf-8">
<title>Zernova Smoking Requisites Trading LLC – Business Card</title>
<link href="https://fonts.googleapis.com/css2?family=Roboto:ital,wght@0,400;0,500;0,700;1,400&display=swap" rel="stylesheet">
<style>
  :root {
    --bg: #b3c0c5;
    --card: #ffffff;
    --ink: #1f1f22;
    --accent: #c0343a;
  }
  * { box-sizing: border-box; margin: 0; padding: 0; }
  html, body { width: 1200px; height: 871px; overflow: hidden; }
  body {
    background: var(--bg);
    font-family: "Roboto", Arial, sans-serif;
    color: var(--ink);
    position: relative;
  }
  .card {
    position: absolute;
    top: 145px;
    width: 340px;
    height: 580px;
    background: var(--card);
    box-shadow: 0 6px 18px rgba(0,0,0,0.18);
  }
  .card--front { left: 220px; }
  .card--back { left: 640px; }
  .frame { position: absolute; left: 0; top: 0; width: 340px; height: 580px; }
  .frame line { stroke: var(--accent); stroke-width: 6; }

  .tagline {
    position: absolute;
    left: 0; right: 0;
    text-align: center;
    font-style: italic;
    font-size: 15px;
    line-height: 18px;
    letter-spacing: 2px;
  }
  .tagline--top { top: 48px; }
  .tagline--bottom { top: 412px; }

  .brand {
    position: absolute;
    left: 0; right: 0;
    display: flex;
    align-items: center;
    justify-content: center;
    gap: 12px;
  }
  .card--front .brand { top: 228px; }
  .card--back .brand { top: 110px; }
  .brand__mark { width: 18px; height: 18px; background: var(--accent); flex: none; }
  .brand__name {
    font-weight: 500;
    color: var(--ink);
    text-transform: uppercase;
    letter-spacing: 3px;
    font-size: 13px;
    line-height: 20px;
  }
  .brand__name strong { display: block; font-weight: 500; font-size: 34px; line-height: 40px; letter-spacing: 6px; }

  .person { position: absolute; top: 262px; left: 0; right: 0; text-align: center; }
  .person__name { font-weight: 700; font-size: 30px; }
  .person__role { color: var(--accent); font-weight: 500; font-size: 22px; margin-top: 2px; }

  .contacts { position: absolute; top: 372px; left: 0; right: 0; text-align: center; list-style: none; }
  .contacts li { margin-bottom: 12px; font-size: 16px; letter-spacing: 3px; }
  .contacts svg { display: block; margin: 0 auto 6px; width: 15px; height: 15px; }
  .contacts svg * { fill: none; stroke: var(--ink); stroke-width: 1.6; }
</style>
</head>
<body>

<section class="card card--front">
  <svg class="frame" viewBox="0 0 340 580" aria-hidden="true">
    <line x1="32" y1="24" x2="308" y2="24"/>
    <line x1="32" y1="21" x2="32" y2="88"/>
    <line x1="308" y1="21" x2="308" y2="128"/>
    <line x1="32" y1="556" x2="308" y2="556"/>
    <line x1="32" y1="559" x2="32" y2="452"/>
    <line x1="308" y1="559" x2="308" y2="492"/>
  </svg>
  <p class="tagline tagline--top">Import Flavoured<br>Tobacco Products<br>and Charcoal</p>
  <div class="brand">
    <span class="brand__mark"></span>
    <p class="brand__name"><strong>Zernova</strong>Smoking Requisites<br>Trading LLC</p>
  </div>
  <p class="tagline tagline--bottom">smoking in a<br>Hookah/Shisha<br>and distribute to the<br>wholesalers and<br>retailers</p>
</section>

<section class="card card--back">
  <svg class="frame" viewBox="0 0 340 580" aria-hidden="true">
    <line x1="32" y1="24" x2="308" y2="24"/>
    <line x1="32" y1="21" x2="32" y2="98"/>
    <line x1="308" y1="21" x2="308" y2="118"/>
    <line x1="32" y1="556" x2="308" y2="556"/>
    <line x1="32" y1="559" x2="32" y2="462"/>
    <line x1="308" y1="559" x2="308" y2="482"/>
  </svg>
  <div class="brand">
    <span class="brand__mark"></span>
    <p class="brand__name"><strong>Zernova</strong>Smoking Requisites<br>Trading LLC</p>
  </div>
  <div class="person">
    <h1 class="person__name">Marek Wolanski</h1>
    <p class="person__role">Partner</p>
  </div>
  <ul class="contacts">
    <li>
      <svg viewBox="0 0 16 16" aria-hidden="true"><path d="M3 2 L6 2 L7 5 L5.5 6.5 Q7 9.5 9.5 10.5 L11 9 L14 10 L14 13 Q8 14 4 9 Q2 6 3 2 Z"/></svg>
      123-456-7890
    </li>
    <li>
      <svg viewBox="0 0 16 16" aria-hidden="true"><rect x="1.5" y="3.5" width="13" height="9"/><path d="M1.5 3.5 L8 9 L14.5 3.5"/></svg>
      merchant@mail.com
    </li>
    <li>
      <svg viewBox="0 0 16 16" aria-hidden="true"><circle cx="8" cy="8" r="6.5"/><ellipse cx="8" cy="8" rx="3" ry="6.5"/><path d="M1.5 8 H14.5 M2.5 4.8 H13.5 M2.5 11.2 H13.5"/></svg>
      weblink.com
    </li>
  </ul>
</section>

</body>
</html>
```